Morning Harbor Community Chapel needs a new Business Card/Letterhead Suite

***** IT DOES NOT HAVE TO FEATURE GREEN AND BROWN in order to be a successful design*****

****FONTS: SF New Republic, 'Morning Harbor'; Nexa Light, 'Community Chapel'****

***We have two locations, with two addresses. So the business card AND letterhead need to include two sets of address information***

We are a growing church in New York in need of a new stationary suite. We have recently adopted a new logo (via a successful PixelGuild project) and need new business cards, letterhead, envelopes, and folders.

We would like to see creative, original designs that are modern and clean/elegant (NOT dated "churchy" graphics that are cheesy).

We need this project worked on immediately, as we need to print new business cards for upcoming programs we have on our schedule. So, the designs need to be solid so that we can move quickly throughout the revision process toward print.

We'd also need editables files, so that we can drop in other staff members names/phone numbers, to be able to print cards for those staff needing them.

Requirements
Must have
• Our logo
• Must be given to us in an editable format (to change names)
Nice to have
• Some examples on grey, or recycled, card stock
• card stock (background) does not have to be white
Should not have
• Any extraneous logo's or symbols

```html
<!DOCTYPE html>
<html lang="en">
<head>
<meta charset="utf-8">
<title>Morning Harbor Community Chapel – Stationery Suite</title>
<link href="https://fonts.googleapis.com/css2?family=Open+Sans:wght@400;600;700&display=swap" rel="stylesheet">
<style>
  :root{
    --green:#427a3b;
    --brown:#655f3a;
    --paper:#ffffff;
    --edge:#8d99ab;
    --ink:#111111;
  }
  *{box-sizing:border-box;margin:0;padding:0}
  html,body{width:1200px;height:1200px;overflow:hidden;background:var(--paper)}
  body{position:relative;font-family:'Open Sans',Arial,sans-serif}
  .sheet{position:absolute;background:var(--paper);border:1px solid var(--edge);overflow:hidden}
  .band{position:absolute}
  .green{background:var(--green)}
  .brown{background:var(--brown)}
  .white{background:var(--paper)}
  .wordmark{position:absolute;font-family:'Open Sans',Arial,sans-serif;font-weight:400;color:var(--green);white-space:nowrap;line-height:1;letter-spacing:-0.02em}
  .small{position:absolute;font-size:7.6px;line-height:12px;white-space:nowrap}

  /* Letterhead */
  .letterhead{left:80px;top:95px;width:715px;height:1010px}
  .letterhead .contact{left:38px;top:38px;color:var(--green);line-height:10.6px}
  .letterhead .web{left:38px;top:93px;color:#fff;line-height:13px}

  /* Business card front */
  .card-front{left:838px;top:95px;width:311px;height:188px}
  .card-front .holder{position:absolute;left:155px;top:39px;color:var(--ink)}
  .holder .name{font-weight:700;font-size:11.2px;line-height:13px}
  .holder .role{font-size:8.6px;line-height:11px}
  .card-front .org{position:absolute;left:152px;top:90px;color:#fff;white-space:nowrap}
  .org .title{font-weight:700;font-size:7.8px;line-height:12px}
  .org .lines{font-size:7.2px;line-height:11px}

  /* Business card back */
  .card-back{left:838px;top:331px;width:311px;height:189px}
  .card-back .web{right:16px;top:13px;color:#fff}

  /* Envelope */
  .envelope{left:380px;top:628px;width:769px;height:371px}
  .envelope .contact{left:20px;top:256px;color:#fff;font-size:7.6px;line-height:12px}
</style>
</head>
<body>

<section class="sheet letterhead" aria-label="Letterhead">
  <div class="band green" style="left:0;top:0;width:100%;height:36px"></div>
  <div class="band brown" style="left:0;top:93px;width:100%;height:13.6px"></div>
  <div class="band white" style="left:563px;top:0;width:38px;height:107px"></div>
  <div class="wordmark" style="right:50px;top:60px;font-size:25px">Morning Harbor</div>
  <div class="small contact">
    No: 45 , Harbor Lane, Bay Town.<br>
    No: 12 , Pier Road, Bay Town.<br>
    +01 55 01234 567<br>
    +01 55 01234 568<br>
    info@morningharbor.org
  </div>
  <div class="small web">www.morningharbor.org</div>
</section>

<section class="sheet card-front" aria-label="Business card front">
  <div class="band brown" style="left:0;top:0;width:100%;height:25px"></div>
  <div class="band green" style="left:0;top:74px;width:100%;height:114px"></div>
  <div class="band white" style="left:66px;top:0;width:26px;height:100%"></div>
  <div class="wordmark" style="left:9px;top:45px;font-size:15.5px">Morning Harbor</div>
  <div class="holder">
    <div class="name">Card Owner Name</div>
    <div class="role">Position</div>
  </div>
  <div class="org">
    <div class="title">Morning Harbor Community Chapel</div>
    <div class="lines">
      No: 45 , Harbor Lane, Bay Town.<br>
      No: 12 , Pier Road, Bay Town.<br>
      T : +01 55 01234 567<br>
      F : +01 55 01234 568<br>
      M: +01 55 01234 569<br>
      E : info@morningharbor.org
    </div>
  </div>
</section>

<section class="sheet card-back" aria-label="Business card back">
  <div class="band green" style="left:0;top:0;width:100%;height:129px"></div>
  <div class="band brown" style="left:0;top:178px;width:100%;height:11px"></div>
  <div class="band white" style="left:66px;top:0;width:26px;height:100%"></div>
  <div class="small web">www.morningharbor.org</div>
  <div class="wordmark" style="left:9px;top:147px;font-size:15.5px">Morning Harbor</div>
</section>

<section class="sheet envelope" aria-label="Envelope">
  <div class="band green" style="left:0;top:0;width:100%;height:38.4px"></div>
  <div class="band brown" style="left:0;top:100px;width:122px;height:271px"></div>
  <div class="band brown" style="left:164px;top:100.8px;width:605px;height:7.2px"></div>
  <div class="band white" style="left:122px;top:0;width:42px;height:100px"></div>
  <div class="wordmark" style="left:27px;top:55px;font-size:27px">Morning Harbor</div>
  <div class="small contact">
    No: 45 , Harbor Lane,<br>
    Bay Town.<br>
    No: 12 , Pier Road,<br>
    Bay Town.<br>
    +01 55 01234 567<br>
    +01 55 01234 568<br>
    info@morningharbor.org<br>
    www.morningharbor.org
  </div>
</section>

</body>
</html>
```